KT Crewing business card

Require business card which includes:
Company name: KT CREWING PTY LTD
Email: Mick@ktcrewing.com.au
Phone: 0431 556 208
ACN: 517 238 649

slogan: Onsite Auto Electrician Labour hire

Details and logo on top side
Logo only on bottom side

colour codes : #F15A29 , #939598

Target Market(s)

Western Australia mining sector

Industry/Entity Type

Mining

Contact Information for Business Card

Require business card which includes: Company name: KT CREWING PTY LTD Email: Mick@ktcrewing.com.au Phone: 0431 556 208 ACN: 517 238 649 slogan: Onsite Auto Electrician Labour hire Details and logo on top side Logo only on bottom side colour codes : #F15A29 , #939598

Colors
EE7325
F08F49
F5BC92
FAE3D3
FDF4ED

Requirements
Must have
• double sided

```html
<!DOCTYPE html>
<html lang="en">
<head>
<meta charset="utf-8">
<title>KT Crewing Business Card</title>
<link rel="stylesheet" href="https://fonts.googleapis.com/css2?family=Montserrat:wght@400;500;700;800&display=swap">
<style>
  :root {
    --orange: #F15A29;
    --grey: #939598;
    --ink: #3a3a3c;
    --paper: #ffffff;
    --backdrop: #1e1e1f;
  }
  * { box-sizing: border-box; margin: 0; padding: 0; }
  html, body {
    width: 1200px; height: 901px; overflow: hidden;
    background: var(--backdrop);
    font-family: "Montserrat", sans-serif;
  }
  .sheet {
    position: relative; width: 1200px; height: 901px;
    display: flex; align-items: center; justify-content: center; gap: 44px;
  }
  .card {
    position: relative;
    width: 530px; height: 322px;
    background: var(--paper);
    border-radius: 30px;
    overflow: hidden;
  }
  .brand {
    position: absolute;
    display: flex; align-items: center; gap: 14px;
  }
  .brand-mark {
    width: 30px; height: 30px; background: var(--grey);
  }
  .brand-name {
    font-weight: 800; color: var(--orange);
    letter-spacing: -0.5px; line-height: 1;
    white-space: nowrap;
  }
  .card-back .brand { left: 50%; top: 50%; transform: translate(-50%, -50%); }
  .card-back .brand-name { font-size: 54px; }
  .card-back .brand-mark { width: 40px; height: 40px; }

  .card-front .brand { right: 34px; top: 56px; }
  .card-front .brand-name { font-size: 36px; }

  .accent-tab {
    position: absolute; left: 0; top: 150px;
    width: 14px; height: 40px; background: var(--orange);
  }
  .details {
    position: absolute; left: 40px; top: 138px;
    color: var(--ink); font-size: 13.5px; line-height: 1.35;
  }
  .person-name {
    color: var(--orange); font-weight: 800; font-size: 19px;
    letter-spacing: 0.3px; line-height: 1.1;
  }
  .person-role { font-size: 13.5px; margin-bottom: 12px; }
  .slogan { margin-bottom: 10px; }
  .contact-line { display: flex; align-items: center; gap: 6px; }
  .contact-line svg { width: 13px; height: 13px; flex: none; }
  .acn { margin-top: 10px; }
  .acn-label { color: var(--orange); font-weight: 700; }
</style>
</head>
<body>
<main class="sheet">
  <section class="card card-back" aria-label="Card back">
    <div class="brand">
      <span class="brand-name">KT Crewing</span>
      <span class="brand-mark"></span>
    </div>
  </section>

  <section class="card card-front" aria-label="Card front">
    <div class="brand">
      <span class="brand-name">KT Crewing</span>
      <span class="brand-mark"></span>
    </div>
    <span class="accent-tab"></span>
    <div class="details">
      <p class="person-name">WARREN HALE</p>
      <p class="person-role">Managing Director</p>
      <p class="slogan">Onsite Auto Electrician<br>Labour hire</p>
      <p class="contact-line">
        <svg viewBox="0 0 24 24" aria-hidden="true"><path fill="var(--orange)" d="M6.6 10.8a15.1 15.1 0 0 0 6.6 6.6l2.2-2.2c.3-.3.7-.4 1-.2 1.1.4 2.3.6 3.6.6.6 0 1 .4 1 1V20c0 .6-.4 1-1 1A17 17 0 0 1 3 4c0-.6.4-1 1-1h3.5c.6 0 1 .4 1 1 0 1.3.2 2.5.6 3.6.1.3 0 .7-.2 1z"/></svg>
        0431 556 208
      </p>
      <p class="contact-line">
        <svg viewBox="0 0 24 24" aria-hidden="true"><path fill="var(--orange)" d="M2 5h20v14H2z"/><path fill="none" stroke="#fff" stroke-width="1.8" d="M2.5 5.5 12 13l9.5-7.5"/></svg>
        Mick@ktcrewing.com.au
      </p>
      <p class="acn"><span class="acn-label">ACN</span>: 517 238 649</p>
    </div>
  </section>
</main>
</body>
</html>
```